Brindell Excavation and Landscaping

I need a double sided card thick with rounded edges. I want an identical card of one of your designs but with my name on it on one side. Othe side I want my name,number under owner operator and a list of what I do. , drainage,grading,trenching stump removal , postholes. Landscaping lawn renovations, and reconfigurations, small to large rip outs and installs,sod work and burms and swails for water run off and plantings the two pictures of cards is what I like

Reason: First time doing this not sure if two days was enough, no one was taking on project so trying to figure out why I posted a picture of what I want so should be relatively easy

Industry/Entity Type

Landscaping

Contact Information for Business Card

Name Ted Brindell
Palm beach county Phone 860-555-0143

Font styles to use
Other font styles liked:
• It's on card I sent second one

Requirements
Must have
• Same colors and look of card at bottom
Nice to have
• All aspects of excavation and landscaping on back of card
• Will add web address at end

```html
<!DOCTYPE html>
<html lang="en">
<head>
<meta charset="utf-8">
<title>Brindell Excavation and Landscaping — Business Card</title>
<link rel="stylesheet" href="https://fonts.googleapis.com/css2?family=Work+Sans:wght@400;500;700;800&display=swap">
<style>
  :root {
    --bg: #ece9e4;
    --card-dark: #262626;
    --card-dark-2: #3b3833;
    --orange: #ec7a30;
    --orange-deep: #e2621f;
    --grey: #5c5c5c;
    --white: #ffffff;
    --shadow: rgba(0, 0, 0, 0.28);
  }
  * { box-sizing: border-box; margin: 0; padding: 0; }
  html, body {
    width: 1200px;
    height: 1000px;
    overflow: hidden;
    background: var(--bg);
    font-family: "Work Sans", Arial, sans-serif;
  }
  .card {
    position: absolute;
    left: 290px;
    width: 620px;
    height: 354px;
    border-radius: 30px;
    overflow: hidden;
    box-shadow: 0 10px 24px var(--shadow);
  }
  /* Front side */
  .card--front { top: 90px; background: var(--card-dark); }
  .front-photo {
    position: absolute;
    inset: 0;
    background:
      radial-gradient(ellipse at 70% 40%, rgba(120, 105, 80, 0.45), transparent 60%),
      radial-gradient(ellipse at 35% 85%, rgba(140, 130, 115, 0.35), transparent 55%),
      linear-gradient(160deg, var(--card-dark) 0%, var(--card-dark-2) 100%);
  }
  .front-brand {
    position: absolute;
    left: 0; right: 0;
    top: 132px;
    text-align: center;
    color: var(--white);
    font-weight: 800;
    font-size: 30px;
    line-height: 1.15;
    letter-spacing: 1px;
    text-transform: uppercase;
  }
  /* Back side */
  .card--back { top: 540px; background: var(--white); }
  .back-panel {
    position: absolute;
    inset: 0;
    background: linear-gradient(135deg, var(--orange) 0%, var(--orange-deep) 100%);
    clip-path: polygon(50% 0, 100% 0, 100% 100%, 66% 100%);
  }
  .back-brand {
    position: absolute;
    left: 40px;
    top: 96px;
    width: 250px;
    color: var(--orange-deep);
    font-weight: 800;
    font-size: 26px;
    line-height: 1.15;
    text-transform: uppercase;
  }
  .services {
    position: absolute;
    left: 0;
    top: 228px;
    width: 392px;
    height: 88px;
    background: var(--grey);
    clip-path: polygon(0 0, 96% 0, 100% 100%, 0 100%);
    padding: 12px 0 0 30px;
    color: var(--white);
    font-size: 15px;
    line-height: 1.4;
    list-style: none;
  }
  .name-tab {
    position: absolute;
    left: 300px;
    top: 38px;
    width: 250px;
    height: 38px;
    background: var(--grey);
    color: var(--white);
    display: flex;
    align-items: center;
    justify-content: center;
    gap: 6px;
    font-size: 18px;
    text-transform: uppercase;
  }
  .name-tab strong { font-weight: 700; }
  .name-tab span { font-weight: 400; font-size: 15px; }
  .contacts {
    position: absolute;
    right: 28px;
    top: 176px;
    list-style: none;
    color: var(--white);
    font-size: 15px;
    text-align: right;
  }
  .contacts li {
    display: flex;
    align-items: center;
    justify-content: flex-end;
    gap: 10px;
    line-height: 26px;
  }
  .contacts svg { width: 14px; height: 14px; flex: none; }
</style>
</head>
<body>
  <section class="card card--front" aria-label="Card front">
    <div class="front-photo" role="img" aria-label="Darkened photograph of an excavator working on a dirt site"></div>
    <div class="front-brand">Brindell<br>Excavation and Landscaping</div>
  </section>

  <section class="card card--back" aria-label="Card back">
    <div class="back-panel"></div>
    <div class="back-brand">Brindell<br>Excavation and Landscaping</div>
    <ul class="services">
      <li>Drainage | Grading | Trenching</li>
      <li>Landscaping lawn renovations</li>
      <li>Small to large rip outs and installs</li>
    </ul>
    <div class="name-tab"><strong>Ted Brindell</strong><span>Owner</span></div>
    <ul class="contacts">
      <li>860-555-0143
        <svg viewBox="0 0 14 14" aria-hidden="true"><rect x="3.5" y="1" width="7" height="12" rx="1.2" fill="none" stroke="#fff" stroke-width="1.4"/><circle cx="7" cy="11" r="0.8" fill="#fff"/></svg>
      </li>
      <li>info@tedbrindell.com
        <svg viewBox="0 0 14 14" aria-hidden="true"><rect x="1" y="3" width="12" height="8.5" fill="#fff"/><path d="M1 3 L7 8 L13 3" fill="none" stroke="#e2621f" stroke-width="1.2"/></svg>
      </li>
      <li>www.brindellexcavation.com
        <svg viewBox="0 0 14 14" aria-hidden="true"><circle cx="6" cy="6" r="4" fill="none" stroke="#fff" stroke-width="1.8"/><line x1="9" y1="9" x2="13" y2="13" stroke="#fff" stroke-width="2"/></svg>
      </li>
    </ul>
  </section>
</body>
</html>
```